Sports Psychology Business Card Design

Need a catchy and unique business card design for our sport psychology practice. We provide mental performance counseling and consulting to performers from all types of industries with a special emphases on athletes.The name of our practice is "Steady Core of Achievement" or "SCA" as is indicated in the logo examples submitted in this brief. Also provided were logos with specific sports referenced which represent sources of our clients from those sports.

Target Market(s)

Executives, Professionals (doctors, lawyers, etc.), Athletes, Entertainers and other performers

Contact Information for Business Card

Need to include our logo (logos provided in this brief).

Font styles to use
Other font styles liked:
• Font can be found in logo

Colors
0792cd
34a7d8
85cae6

Requirements
Must have
• Our logo and reference to our provision of mental performance counseling/consulting/coaching
Nice to have
• References to sports that our athletes play as provided in the brief.
Should not have
• This is not a general wellness consulting practice. Our focus is on consulting to improve mental performance.

```html
<!DOCTYPE html>
<html lang="en">
<head>
<meta charset="utf-8">
<title>Steady Core of Achievement – Business Card</title>
<link rel="stylesheet" href="https://fonts.googleapis.com/css2?family=Open+Sans:wght@400;600;700&family=Cutive&display=swap">
<style>
  :root {
    --blue-deep: #0792cd;
    --blue-mid: #34a7d8;
    --blue-light: #85cae6;
    --paper: #ffffff;
    --text: #111111;
  }
  * { margin: 0; padding: 0; box-sizing: border-box; }
  html, body {
    width: 1200px;
    height: 723px;
    overflow: hidden;
    background: var(--paper);
  }
  .card {
    position: relative;
    width: 1200px;
    height: 723px;
    background: var(--paper);
    border: 1.5px solid var(--blue-deep);
    font-family: "Open Sans", Arial, sans-serif;
    color: var(--text);
    overflow: hidden;
  }
  .card-shapes {
    position: absolute;
    inset: 0;
    width: 1200px;
    height: 723px;
  }
  .holder-name {
    position: absolute;
    top: 88px;
    left: 0;
    width: 1200px;
    text-align: center;
    font-size: 44px;
    font-weight: 400;
    letter-spacing: 0.2px;
  }
  .holder-name strong { font-weight: 700; }
  .brand-name {
    position: absolute;
    top: 186px;
    left: 0;
    width: 1200px;
    text-align: center;
    font-size: 160px;
    line-height: 1;
    font-weight: 600;
    color: var(--blue-mid);
    letter-spacing: 6px;
  }
  .tagline {
    position: absolute;
    top: 383px;
    left: 0;
    width: 1200px;
    text-align: center;
    font-family: "Cutive", "Courier New", serif;
    font-size: 30px;
    color: var(--text);
  }
  .services {
    position: absolute;
    top: 440px;
    left: 0;
    width: 1200px;
    text-align: center;
    font-size: 20px;
    font-weight: 600;
    letter-spacing: 1.5px;
    text-transform: uppercase;
    color: var(--blue-deep);
  }
  .address {
    position: absolute;
    top: 540px;
    left: 62px;
    display: flex;
    align-items: center;
    gap: 10px;
    font-size: 22px;
    color: var(--text);
  }
  .address svg { width: 20px; height: 26px; }
  .contact-row {
    position: absolute;
    top: 638px;
    left: 38px;
    display: flex;
    align-items: center;
    gap: 8px;
    font-size: 23px;
    font-weight: 700;
    color: var(--paper);
    white-space: nowrap;
  }
  .contact-item {
    display: flex;
    align-items: center;
    gap: 7px;
    margin-right: 12px;
  }
  .contact-item svg { width: 32px; height: 26px; }
</style>
</head>
<body>
<div class="card">
  <svg class="card-shapes" viewBox="0 0 1200 723" aria-hidden="true">
    <path d="M0 0 H396 Q411 0 411 16 Q411 32 396 32 H0 Z" fill="var(--blue-mid)"/>
    <path d="M470 0 H1200 V41 H520 Q492 41 478 22 Z" fill="var(--blue-light)"/>
    <path d="M460 0 H1200 V31 H512 Q486 31 472 14 Z" fill="var(--blue-deep)"/>
    <path d="M0 574 H870 Q894 574 908 592 L986 723 H0 Z" fill="var(--blue-light)"/>
    <path d="M0 583 H860 Q884 583 898 600 L972 723 H0 Z" fill="var(--blue-deep)"/>
    <path d="M982 585 H1200 V723 H1062 L972 600 Q966 585 982 585 Z" fill="var(--blue-mid)"/>
  </svg>

  <h1 class="holder-name"><strong>Dana</strong> Whitfield</h1>
  <div class="brand-name">SCA</div>
  <p class="tagline">The Steady Core Of Achievement</p>
  <p class="services">Mental Performance Counseling &amp; Consulting</p>

  <p class="address">
    <svg viewBox="0 0 20 26" aria-hidden="true">
      <path d="M10 0 C4.5 0 0 4.3 0 9.6 C0 16.5 10 26 10 26 S20 16.5 20 9.6 C20 4.3 15.5 0 10 0 Z" fill="var(--blue-deep)"/>
      <circle cx="10" cy="9.6" r="3.6" fill="var(--paper)"/>
    </svg>
    1200 East Harbor Ave. Suite 210, Lane street,
  </p>

  <div class="contact-row">
    <span class="contact-item">
      <svg viewBox="0 0 32 26" aria-hidden="true">
        <path d="M2 9 Q16 -1 30 9 L27 13 L22 11 L21 7 Q16 5 11 7 L10 11 L5 13 Z" fill="var(--paper)"/>
        <path d="M8 13 H24 L28 25 H4 Z" fill="var(--paper)"/>
        <g fill="var(--blue-deep)">
          <rect x="11" y="15" width="2.4" height="2.4"/><rect x="15" y="15" width="2.4" height="2.4"/><rect x="19" y="15" width="2.4" height="2.4"/>
          <rect x="10" y="19" width="2.4" height="2.4"/><rect x="15" y="19" width="2.4" height="2.4"/><rect x="20" y="19" width="2.4" height="2.4"/>
        </g>
      </svg>
      +555-014-2290
    </span>
    <span class="contact-item">
      <svg viewBox="0 0 32 26" aria-hidden="true">
        <rect x="2" y="3" width="28" height="20" fill="none" stroke="var(--paper)" stroke-width="2"/>
        <path d="M2 3 L16 15 L30 3 M2 23 L12 12 M30 23 L20 12" fill="none" stroke="var(--paper)" stroke-width="2"/>
      </svg>
      Email:dana@thesca.co
    </span>
    <span class="contact-item">
      <svg viewBox="0 0 28 28" aria-hidden="true">
        <g fill="none" stroke="var(--paper)" stroke-width="2">
          <circle cx="14" cy="14" r="12"/>
          <ellipse cx="14" cy="14" rx="5.5" ry="12"/>
          <path d="M2 14 H26 M4 8 H24 M4 20 H24 M14 2 V26"/>
        </g>
      </svg>
      www.thesca.com
    </span>
  </div>
</div>
</body>
</html>
```